GLENWICK GROOVE 2014 - Halloween Party

I need a 8.5x11 poster that can also be a jpeg for facebook and run as a display ad in print. I would like a facebook cover and profile picture that matches the poster. This is our 8th annual Halloween costume party and is our biggest event of the year.

Copy is as follows: (no particular order

8th Annual GLENWICK GROOVE
Halloween Costume Party
FRIDAY October 31st (need to emphasize date, usually I do it on Saturday.)
$400 in CASH PRIZES awarded at 9pm AND Midnight
DJ 7pm-2am in the tavern
Live music by VELVET PARROTS in the back room. 9pm.
Drink Specials, Munchies
$5 cover in advance, $10 at the door.
Birch Hollow Lodge, 4183 County Road 71, Hillsdale, NY

Target Market(s)

We are a bar and we have live music and a DJ for this party and are awarding for prizes for the best costumes (and other costumer categories.)

Industry/Entity Type

House

Font styles to use
Other font styles liked:
• halloween, spooky but readable

Requirements
Must have
• Must communicate the details clearly, be able to read from a distance. Due to the amount of Information we need to convey, I am willng to go 8x14 poster size. The emphasis should really be on "Glenwick Groove". "8th annual" is not very important and should be weighted less than Glenwick Groove.
Should not have
• shouldn't be too scary. I've had shop owners tell me that some are too scary to hang in their stores.

```html
<!DOCTYPE html>
<html lang="en">
<head>
<meta charset="utf-8">
<title>Glenwick Groove – Halloween Costume Party</title>
<link rel="stylesheet" href="https://fonts.googleapis.com/css2?family=Creepster&family=Luckiest+Guy&family=Metal+Mania&display=swap">
<style>
  :root {
    --black: #000000;
    --blood: #7a0c06;
    --ember: #b3200c;
    --flame: #f36a12;
    --gold: #ffd94a;
    --cream: #fff6d8;
    --lime: #9be31c;
    --leaf: #3f8f10;
    --orange: #ff9a1c;
  }
  * { margin: 0; padding: 0; box-sizing: border-box; }
  html, body { width: 1000px; height: 1200px; overflow: hidden; background: var(--black); }
  .poster { position: relative; width: 1000px; height: 1200px; background: var(--black); }
  .panel {
    position: absolute; left: 40px; top: 0; width: 920px; height: 1200px;
    background: radial-gradient(ellipse at 50% 70%, #c8300f 0%, var(--ember) 35%, var(--blood) 80%, #4a0603 100%);
    box-shadow: inset 0 0 0 6px #ff8a1a, inset 0 0 30px 14px #f4a324, inset 0 0 70px 20px #c43a0c;
  }
  .art { position: absolute; }
  .skull { width: 140px; height: 200px; border-radius: 45% 45% 40% 40%;
    background: radial-gradient(circle at 50% 62%, #efe3c4 0%, #cbb48a 38%, #ff8a1a 60%, rgba(255,120,20,0) 75%); }
  .skull-left { left: 92px; top: 195px; }
  .skull-right { left: 765px; top: 195px; }
  .flame-wings { left: 80px; top: 760px; width: 850px; height: 130px;
    background: radial-gradient(ellipse at 50% 50%, rgba(255,220,120,.9) 0%, rgba(246,128,24,.75) 35%, rgba(200,50,10,0) 70%); }
  .pumpkin { left: 378px; top: 695px; width: 258px; height: 232px; border-radius: 48% 48% 44% 44%;
    background: radial-gradient(circle at 50% 45%, #ffe27a 0%, #ff9a1c 30%, #e05a0a 65%, #9a2c05 100%); }
  .line { position: absolute; left: 0; width: 1000px; text-align: center; white-space: nowrap; }
  .annual { left: 222px; width: auto; top: 50px; font: 38px/1 "Creepster", cursive;
    color: var(--cream); text-shadow: 0 0 6px var(--flame), 2px 2px 0 #5a0a02; }
  .title { font-family: "Metal Mania", "Creepster", cursive; color: #2a0a05;
    -webkit-text-stroke: 3px var(--flame); text-shadow: 0 0 14px var(--flame), 0 0 30px #ff4a0a; letter-spacing: 2px; }
  .title-top { top: 98px; font-size: 110px; line-height: 1; }
  .title-bottom { top: 205px; font-size: 175px; line-height: 1; }
  .party { top: 425px; font: 36px/1 "Creepster", cursive; color: var(--cream); text-shadow: 2px 2px 0 #3a0502; letter-spacing: 1px; }
  .green { font-family: "Luckiest Guy", sans-serif; color: var(--gold);
    -webkit-text-stroke: 2px var(--leaf); text-shadow: 3px 3px 0 #1f4a06, 0 0 8px rgba(0,0,0,.5); }
  .date { top: 488px; font-size: 66px; line-height: 1; letter-spacing: 2px; }
  .prizes { top: 588px; font-size: 54px; line-height: 1; letter-spacing: 2px; }
  .awarded { top: 662px; font-size: 28px; line-height: 1; color: var(--lime); -webkit-text-stroke: 1px #1f4a06; }
  .tavern { top: 935px; font-size: 56px; line-height: 1; letter-spacing: 2px; }
  .cover { position: absolute; left: 100px; top: 733px; width: 210px; text-align: center;
    font-family: "Luckiest Guy", sans-serif; color: var(--gold); text-shadow: 2px 2px 0 #3a0502; }
  .cover .price { font-size: 40px; line-height: 1.05; }
  .cover .note { font-size: 20px; line-height: 1.2; color: var(--cream); margin-bottom: 10px; }
  .live { top: 1020px; font: 27px/1 "Creepster", cursive; color: var(--cream); letter-spacing: 1px; text-shadow: 2px 2px 0 #3a0502; }
  .specials { top: 1066px; font: 36px/1 "Creepster", cursive; color: var(--orange); letter-spacing: 1px; text-shadow: 2px 2px 0 #3a0502; }
  .venue { top: 1122px; font: 26px/1 "Creepster", cursive; color: var(--lime); letter-spacing: 1px; text-shadow: 2px 2px 0 #1f2a04; }
</style>
</head>
<body>
<main class="poster">
  <div class="panel"></div>
  <div class="art skull skull-left" role="img" aria-label="Flaming skull illustration"></div>
  <div class="art skull skull-right" role="img" aria-label="Flaming skull illustration"></div>

  <p class="line annual">8th Annual</p>
  <h1>
    <span class="line title title-top">GLENWICK</span>
    <span class="line title title-bottom">GROOVE</span>
  </h1>
  <p class="line party">Halloween Costume Party</p>
  <p class="line green date">FRIDAY OCTOBER 31ST</p>
  <p class="line green prizes">$400 IN CASH PRIZES</p>
  <p class="line green awarded">AWARDED AT 9PM AND MIDNIGHT</p>

  <div class="art flame-wings" role="img" aria-label="Fiery wings spreading from the pumpkin"></div>
  <div class="art pumpkin" role="img" aria-label="Glowing jack-o'-lantern illustration"></div>

  <div class="cover">
    <div class="price">$5</div>
    <div class="note">COVER IN ADVANCE,</div>
    <div class="price">$10</div>
    <div class="note">AT THE DOOR.</div>
  </div>

  <p class="line green tavern">DJ 7PM-2AM IN THE TAVERN</p>
  <p class="line live">Live music by VELVET PARROTS in the back room. 9PM.</p>
  <p class="line specials">Drink Specials, Munchies</p>
  <p class="line venue">Birch Hollow Lodge, 4183 County Road 71, Hillsdale, NY</p>
</main>
</body>
</html>
```